Ridgeline Elite

Letter Head, Envelope, Business Cards, Social Media Banner (FB/Twitter), Social Media Icon, Social Media Announcement Template...

We are a Softball Team/Organization

Target Market(s)

High School Student-Athletes (softball players) and their parents

Font styles to use
Serif

Requirements
Must have
• Logo & Colors
Must POP and say WOW
Common theme amongst all designs

```html
<!DOCTYPE html>
<html lang="en">
<head>
<meta charset="utf-8">
<title>Ridgeline Elite – Business Card</title>
<link rel="stylesheet" href="https://fonts.googleapis.com/css2?family=Zilla+Slab:wght@400;600;700&display=swap">
<style>
  :root {
    --navy: #1f3866;
    --navy-text: #1d3563;
    --silver: #c7cedb;
    --stripe: #b9c0cf;
    --paper: #ffffff;
    --ink: #2a2a2a;
    --backdrop: #e9ebef;
  }
  * { margin: 0; padding: 0; box-sizing: border-box; }
  html, body { width: 1200px; height: 960px; overflow: hidden; }
  body {
    background: var(--backdrop);
    font-family: "Zilla Slab", Georgia, serif;
    position: relative;
  }
  .card {
    position: absolute;
    left: 250px;
    width: 700px;
    height: 400px;
    overflow: hidden;
    box-shadow: 0 6px 18px rgba(0,0,0,.18);
  }
  .card--back { top: 50px; background: var(--navy); }
  .card--front { top: 510px; background: var(--paper); }

  .brand {
    position: absolute;
    font-weight: 700;
    text-transform: uppercase;
    letter-spacing: .06em;
    line-height: 1;
  }
  .card--back .brand {
    color: var(--silver);
    font-size: 56px;
    left: 0; right: 0; top: 168px;
    text-align: center;
  }
  .card--front .brand {
    color: var(--navy-text);
    font-size: 26px;
    right: 44px; top: 56px;
  }

  .wave { position: absolute; left: 0; top: 0; width: 700px; height: 400px; }

  .person { position: absolute; left: 40px; top: 178px; }
  .person__name { color: var(--navy-text); font-size: 25px; font-weight: 400; }
  .person__role { color: var(--ink); font-size: 14px; margin-top: 2px; }

  .address {
    position: absolute; left: 80px; top: 272px;
    color: var(--ink); font-size: 15px; line-height: 1.2; font-style: normal;
  }
  .contacts {
    position: absolute; left: 58px; top: 314px;
    list-style: none; color: var(--ink); font-size: 15px;
  }
  .contacts li { display: flex; align-items: center; gap: 12px; height: 21px; }
  .contacts svg { width: 12px; height: 12px; fill: var(--navy-text); flex: none; }
</style>
</head>
<body>
  <section class="card card--back" aria-label="Business card back">
    <div class="brand">Ridgeline Elite</div>
  </section>

  <section class="card card--front" aria-label="Business card front">
    <svg class="wave" viewBox="0 0 700 400" aria-hidden="true">
      <path d="M150,400 C320,392 420,168 700,150 L700,158 C440,178 330,396 170,400 Z" fill="var(--stripe)"/>
      <path d="M170,400 C330,396 440,190 700,166 L700,400 Z" fill="var(--navy)"/>
    </svg>

    <div class="brand">Ridgeline Elite</div>

    <div class="person">
      <h1 class="person__name">Marissa Coldwell</h1>
      <p class="person__role">Founder &amp; CEO</p>
    </div>

    <address class="address">
      418 Meadow Lane<br>
      Topeka, KS 66604
    </address>

    <ul class="contacts">
      <li>
        <svg viewBox="0 0 24 24"><path d="M6.6 10.8a15.1 15.1 0 0 0 6.6 6.6l2.2-2.2c.3-.3.7-.4 1-.2 1.1.4 2.3.6 3.6.6.6 0 1 .4 1 1V20c0 .6-.4 1-1 1C10.6 21 3 13.4 3 4c0-.6.4-1 1-1h3.5c.6 0 1 .4 1 1 0 1.3.2 2.5.6 3.6.1.3 0 .7-.2 1z"/></svg>
        <span>02 555 318 2047</span>
      </li>
      <li>
        <svg viewBox="0 0 24 24"><path d="M2 5h20v2l-10 6L2 7zM2 9.3l10 6 10-6V19H2z"/></svg>
        <span>info@ridgelineelite.com</span>
      </li>
      <li>
        <svg viewBox="0 0 24 24"><path d="M12 2a10 10 0 1 0 0 20 10 10 0 0 0 0-20zm6.9 6h-2.9a15.6 15.6 0 0 0-1.4-3.6A8 8 0 0 1 18.9 8zM12 4c.8 1.2 1.5 2.5 1.9 4h-3.8c.4-1.5 1.1-2.8 1.9-4zM4.3 14a8 8 0 0 1 0-4h3.4a16.5 16.5 0 0 0 0 4zm.8 2h2.9c.3 1.3.8 2.5 1.4 3.6A8 8 0 0 1 5.1 16zM8 8H5.1a8 8 0 0 1 4.3-3.6C8.8 5.5 8.3 6.7 8 8zm4 12c-.8-1.2-1.5-2.5-1.9-4h3.8c-.4 1.5-1.1 2.8-1.9 4zm2.3-6H9.7a14.7 14.7 0 0 1 0-4h4.6a14.7 14.7 0 0 1 0 4zm.3 5.6c.6-1.1 1.1-2.3 1.4-3.6h2.9a8 8 0 0 1-4.3 3.6zm1.7-5.6a16.5 16.5 0 0 0 0-4h3.4a8 8 0 0 1 0 4z"/></svg>
        <span>www.ridgelineelite.com</span>
      </li>
    </ul>
  </section>
</body>
</html>
```